Business Card Design

We need a business card design that can also be aplied for postcards. We are a small indie record company that also do consulting, and development of independat artitst . I already have the name and the basic idea of what i am looking for but i am open to any suggestion.
Info for the card
Name of the company : Velmora Records
NAME : Tomas Invaldi
PHONE : 208-5536142
EMAIL : hello@velmorarecords.example
WEB: www.velmorarecords.example
Target Market(s)
Male - Female independent musicians ages 18 to 45
Industry/Entity Type
Record Company
Contact Information for Business Card
Independant records company that also works in consulting for music business models for independent artists
Look and feel
Each slider illustrates characteristics of the customer's brand and the style your logo design should communicate.

```html
<!DOCTYPE html>
<html lang="en">
<head>
<meta charset="utf-8">
<title>Velmora Records — Business Card</title>
<link href="https://fonts.googleapis.com/css2?family=Lobster&family=Open+Sans:wght@400;600&display=swap" rel="stylesheet">
<style>
  :root {
    --page: #e9e7e3;
    --card: #ffffff;
    --card-shade: #e6e6e6;
    --red: #d10a0a;
    --black: #1f1f1f;
    --ink: #2a2a2a;
    --rule: #9a9a9a;
  }
  * { margin: 0; padding: 0; box-sizing: border-box; }
  html, body { width: 1200px; height: 1024px; overflow: hidden; }
  body {
    background: var(--page);
    font-family: "Open Sans", Arial, sans-serif;
    color: var(--ink);
    position: relative;
  }
  .card {
    position: absolute;
    left: 190px;
    width: 820px;
    height: 468px;
    background: linear-gradient(135deg, var(--card) 40%, var(--card-shade) 100%);
    box-shadow: 0 6px 18px rgba(0,0,0,.18);
    overflow: hidden;
  }
  .card-front { top: 36px; }
  .card-back { top: 520px; }

  /* Front */
  .front-band {
    position: absolute; left: 0; right: 0; bottom: 0; height: 58px;
    background: var(--red);
  }
  .front-band::after {
    content: ""; position: absolute; right: 0; top: 0; bottom: 0; width: 130px;
    background: var(--black);
  }
  .front-divider {
    position: absolute; left: 370px; top: 0; bottom: 58px; width: 1px;
    background: var(--rule);
  }
  .brand {
    position: absolute; display: flex; align-items: center; gap: 14px;
  }
  .brand-disc { border-radius: 50%; background: var(--black); flex: none; }
  .brand-name { font-weight: 600; color: var(--ink); white-space: nowrap; }
  .card-front .brand { left: 34px; top: 160px; }
  .card-front .brand-disc { width: 84px; height: 84px; }
  .card-front .brand-name { font-size: 24px; }

  .person {
    position: absolute; right: 50px; top: 52px;
    display: flex; align-items: center; gap: 18px;
  }
  .person-rule { width: 200px; height: 1px; background: var(--rule); }
  .person-name {
    font-family: "Lobster", cursive; font-size: 36px; color: var(--red);
  }
  .contacts {
    position: absolute; left: 405px; top: 240px;
    list-style: none; display: flex; flex-direction: column; gap: 16px;
  }
  .contacts li { display: flex; align-items: center; gap: 16px; font-size: 19px; }
  .contacts svg { width: 20px; height: 20px; flex: none; }

  /* Back */
  .back-band {
    position: absolute; left: 0; top: 0; bottom: 0; width: 78px;
    background: var(--red);
  }
  .back-band::after {
    content: ""; position: absolute; left: 0; right: 0; bottom: 0; height: 96px;
    background: var(--black);
  }
  .card-back .brand { left: 190px; top: 159px; gap: 28px; }
  .card-back .brand-disc { width: 150px; height: 150px; }
  .card-back .brand-name { font-size: 44px; }
</style>
</head>
<body>

<section class="card card-front" aria-label="Business card front">
  <div class="front-divider"></div>
  <div class="brand">
    <span class="brand-disc"></span>
    <span class="brand-name">Velmora Records</span>
  </div>
  <div class="person">
    <span class="person-rule"></span>
    <span class="person-name">Tomas Invaldi</span>
  </div>
  <ul class="contacts">
    <li>
      <svg viewBox="0 0 24 24" aria-hidden="true"><path fill="#d10a0a" d="M6.6 10.8a15.1 15.1 0 0 0 6.6 6.6l2.2-2.2c.3-.3.7-.4 1-.2 1.1.4 2.3.6 3.6.6.6 0 1 .4 1 1V20c0 .6-.4 1-1 1C10.6 21 3 13.4 3 4c0-.6.4-1 1-1h3.5c.6 0 1 .4 1 1 0 1.3.2 2.5.6 3.6.1.3 0 .7-.2 1z"/></svg>
      <span>208-5536142</span>
    </li>
    <li>
      <svg viewBox="0 0 24 24" aria-hidden="true"><rect x="2" y="5" width="20" height="14" rx="2" fill="#d10a0a"/><path d="M3 6l9 7 9-7" fill="none" stroke="#fff" stroke-width="1.6"/></svg>
      <span>hello@velmorarecords.example</span>
    </li>
    <li>
      <svg viewBox="0 0 24 24" aria-hidden="true"><circle cx="12" cy="12" r="10" fill="#d10a0a"/><path d="M2 12h20M12 2c3 3 3 17 0 20M12 2c-3 3-3 17 0 20" fill="none" stroke="#fff" stroke-width="1.4"/></svg>
      <span>www.velmorarecords.example</span>
    </li>
  </ul>
  <div class="front-band"></div>
</section>

<section class="card card-back" aria-label="Business card back">
  <div class="back-band"></div>
  <div class="brand">
    <span class="brand-disc"></span>
    <span class="brand-name">Velmora Records</span>
  </div>
</section>

</body>
</html>
```